Marlow crest Letter head

Need a heeder and footer for 8.5 x 11 paper
2 inch top header, 1.5 inch bottom footer
Add logo, agent pictures, names and titles (Broker), office picture with address
Marlow Crest Real Estate
20387 Route 512
Cedar Hollow, ST 00142
Please make phone # large (555) 304-7182
MarlowCrestRealEstate.example

```html
<!DOCTYPE html>
<html lang="en">
<head>
<meta charset="utf-8">
<title>Marlow Crest Real Estate Letterhead</title>
<link href="https://fonts.googleapis.com/css2?family=Open+Sans:wght@400;600&family=Roboto:wght@400;500&family=Roboto+Slab:wght@500&display=swap" rel="stylesheet">
<style>
  :root {
    --backdrop: #e9e6e1;
    --paper-top: #ffffff;
    --paper-mid: #f4f4f5;
    --paper-bottom: #eeeef0;
    --ink: #3c3c3c;
    --ink-dark: #2b2b2b;
    --brand-red: #c8202f;
    --brand-navy: #1f3566;
    --photo-tone: #e0566f;
    --photo-tone-light: #e8c9a6;
    --signature-tone: #d9d9dc;
  }
  * { box-sizing: border-box; margin: 0; padding: 0; }
  html, body {
    width: 1084px; height: 1200px; overflow: hidden;
    background: var(--backdrop);
  }
  .letterhead {
    position: absolute; left: 102px; top: 29px;
    width: 880px; height: 1142px;
    background: linear-gradient(180deg, var(--paper-top) 0%, var(--paper-mid) 30%, var(--paper-top) 50%, var(--paper-mid) 85%, var(--paper-bottom) 100%);
    box-shadow: 0 4px 14px rgba(0,0,0,.18);
    overflow: hidden;
    font-family: "Open Sans", sans-serif;
    color: var(--ink);
  }
  .brand {
    position: absolute; left: 84px; top: 98px; width: 200px;
    display: flex; align-items: center; gap: 10px;
    font-family: "Open Sans", sans-serif; font-weight: 600;
    color: var(--brand-navy); font-size: 22px; line-height: 1.15;
  }
  .brand-mark { width: 14px; height: 14px; background: var(--brand-navy); flex: none; }
  .contact {
    position: absolute; left: 520px; top: 76px;
    font-family: "Roboto", sans-serif; font-size: 16px; line-height: 20px;
    color: var(--ink-dark); list-style: none;
  }
  .contact li { display: flex; align-items: center; gap: 6px; }
  .contact .phone { font-size: 17px; font-weight: 500; }
  .contact svg { width: 14px; height: 14px; flex: none; fill: var(--brand-red); }
  .letter {
    position: absolute; left: 79px; top: 262px; width: 722px;
    font-size: 15.3px; line-height: 22px;
  }
  .letter p { text-align: justify; margin-bottom: 22px; }
  .letter .closing { margin-top: 0; }
  .signature {
    position: absolute; left: 80px; top: 841px; width: 100px; height: 92px;
    background: var(--signature-tone); border-radius: 6px;
  }
  .agent-photo {
    position: absolute; left: 0; top: 977px; width: 138px; height: 165px;
    background: linear-gradient(180deg, var(--photo-tone-light) 0%, var(--photo-tone) 70%);
  }
  .agent-name {
    position: absolute; left: 167px; top: 1100px;
    font-family: "Roboto Slab", serif; font-weight: 500; font-size: 16px;
    color: var(--brand-red);
  }
  .agent-name .title { color: var(--brand-navy); font-size: 14px; }
</style>
</head>
<body>
<main class="letterhead">
  <header>
    <div class="brand"><span class="brand-mark"></span><span>Marlow Crest<br>Real Estate</span></div>
    <ul class="contact">
      <li>20387 Route 512</li>
      <li>Cedar Hollow, ST 00142</li>
      <li class="phone"><svg viewBox="0 0 16 16"><path d="M3.6 1.2l2.4 2.6-1.3 2a9 9 0 0 0 5.4 5.4l2-1.3 2.6 2.4-1.4 2.3C7.2 16.1-.1 8.8 1.2 2.7z"/></svg>(555) 304-7182</li>
      <li><svg viewBox="0 0 16 16"><path d="M1 3h14v1.2L8 9 1 4.2z"/><path d="M1 5.8l7 4.8 7-4.8V13H1z"/></svg>info@MarlowCrestRealEstate.example</li>
      <li><svg viewBox="0 0 16 16"><circle cx="8" cy="8" r="7"/><path d="M1 8h14M8 1c-3 3.5-3 10.5 0 14M8 1c3 3.5 3 10.5 0 14" stroke="#fff" stroke-width="1.2" fill="none"/></svg>MarlowCrestRealEstate.example</li>
    </ul>
  </header>

  <section class="letter">
    <p class="salutation">Dear customer,</p>
    <p>Lorem ipsum dolor sit amet, consectetur adipisicing elit, sed do eiusmod tempor incididunt ut labore et dolore magna aliqua. Ut enim ad minim veniam, quis nostrud exercitation ullamco laboris nisi ut aliquip ex ea commodo consequat. Duis aute irure dolor in reprehenderit in voluptate velit esse cillum dolore eu fugiat nulla pariatur. Excepteur sint occaecat cupidatat non proident, sunt in culpa qui officia deserunt mollit anim id est laborum.</p>
    <p>Lorem ipsum dolor sit amet, consectetur adipisicing elit, sed do eiusmod tempor incididunt ut labore et dolore magna aliqua. Ut enim ad minim veniam, quis nostrud exercitation ullamco laboris nisi ut aliquip ex ea commodo consequat. Duis aute irure dolor in reprehenderit in voluptate velit esse cillum dolore eu fugiat nulla pariatur. Excepteur sint occaecat cupidatat non proident, sunt in culpa qui officia deserunt mollit anim id est laborum.</p>
    <p>Lorem ipsum dolor sit amet, consectetur adipisicing elit, sed do eiusmod tempor incididunt ut labore et dolore magna aliqua. Ut enim ad minim veniam, quis nostrud exercitation ullamco laboris nisi ut aliquip ex ea commodo consequat. Duis aute irure dolor in reprehenderit in voluptate velit esse cillum dolore eu fugiat nulla pariatur. Excepteur sint occaecat cupidatat non proident, sunt in culpa qui officia deserunt mollit anim id est laborum.</p>
    <p>Lorem ipsum dolor sit amet, consectetur adipisicing elit, sed do eiusmod tempor incididunt ut labore et dolore magna aliqua. Ut enim ad minim veniam, quis nostrud exercitation ullamco laboris nisi ut aliquip ex ea commodo consequat. Duis aute irure dolor in reprehenderit.</p>
    <p class="closing">Yours Sincerely,</p>
  </section>

  <div class="signature" role="img" aria-label="Handwritten signature of the broker"></div>

  <footer>
    <div class="agent-photo" role="img" aria-label="Portrait photo of broker Dana Whitfield"></div>
    <p class="agent-name">Dana Whitfield <span class="title">• Broker</span></p>
  </footer>
</main>
</body>
</html>
```